Wine Bottle Label Logo Design

My fiancé and I are getting married in September and we made homemade wine which will be given to the guests as a wedding favor. We need label/logo for our wine bottles. We were looking for something rustic yet modern and simple. We had an idea for beige and cranberry colored wine stained, weathered, imperfect heart. Things that will need to be incorporated into the label design are as follows:
Our last name and also the name of the wine: Fusaldi
The year: 2012
Where is says Alcohol Content on a wine bottle normally write: Alcohol: Deceiving% by vol.
Type of wine: Red Wine
Incorporate our wedding date: Foot Stomped and Bottled for Nadia and Gus's Wedding Day 9/28/13
Wedding

```html
<!DOCTYPE html>
<html lang="en">
<head>
<meta charset="UTF-8">
<title>Fusaldi Red Wine – Wedding Favor Labels</title>
<link rel="stylesheet" href="https://fonts.googleapis.com/css2?family=Libre+Baskerville:ital,wght@0,700;1,700&family=Open+Sans:ital,wght@0,400;0,700;1,700&display=swap">
<style>
  :root {
    --backdrop: #3b3b3d;
    --label-cream: #f3e2bf;
    --label-cream-light: #f8ecd3;
    --pattern-ivory: #f7f1e6;
    --pattern-gold: #d9c29a;
    --ink-slate: #434b5e;
    --ink-dark: #2c2a28;
    --cranberry: #a3182a;
    --wordmark-gold: #8f6a3c;
  }

  * { box-sizing: border-box; margin: 0; padding: 0; }

  html, body {
    width: 1200px;
    height: 1000px;
    overflow: hidden;
  }

  body {
    background: var(--backdrop);
    position: relative;
    font-family: "Open Sans", Arial, sans-serif;
  }

  .label {
    position: absolute;
    top: 90px;
    width: 300px;
    height: 820px;
    background: linear-gradient(90deg, var(--label-cream) 0%, var(--label-cream-light) 45%, var(--label-cream) 100%);
    border-radius: 6px;
    overflow: hidden;
  }

  .label--plain { left: 250px; }
  .label--patterned { left: 650px; }

  .heart-pattern {
    position: absolute;
    top: 0;
    width: 46px;
    height: 100%;
    background: linear-gradient(180deg, var(--pattern-ivory), var(--pattern-gold) 50%, var(--pattern-ivory));
  }
  .heart-pattern--left { left: 0; }
  .heart-pattern--right { right: 0; }

  .label__header {
    position: absolute;
    top: 48px;
    left: 0;
    width: 100%;
    text-align: center;
  }

  .alcohol {
    font-family: "Open Sans", Arial, sans-serif;
    font-weight: 700;
    font-style: italic;
    font-size: 15px;
    color: var(--ink-slate);
  }

  .vintage {
    margin-top: 12px;
    font-weight: 700;
    font-size: 16px;
    color: var(--ink-dark);
  }

  .dedication {
    margin-top: 6px;
    font-size: 10px;
    line-height: 1.2;
    color: var(--ink-dark);
  }

  .wine-type {
    margin-top: 6px;
    font-family: "Libre Baskerville", Georgia, serif;
    font-weight: 700;
    font-size: 20px;
    color: var(--cranberry);
  }

  .wordmark {
    position: absolute;
    left: 50%;
    top: 490px;
    transform: translate(-50%, -50%) rotate(-90deg);
    white-space: nowrap;
    display: flex;
    align-items: center;
    gap: 18px;
  }

  .wordmark__name {
    font-family: "Libre Baskerville", Georgia, serif;
    font-weight: 700;
    font-size: 112px;
    line-height: 1;
    color: var(--wordmark-gold);
  }

  .wordmark__dot {
    width: 34px;
    height: 34px;
    border-radius: 50%;
    background: var(--cranberry);
  }

  .label__footer {
    position: absolute;
    bottom: 48px;
    left: 0;
    width: 100%;
    text-align: center;
    color: var(--ink-dark);
  }

  .wedding-date { font-size: 11px; }

  .volume {
    margin-top: 4px;
    font-weight: 700;
    font-size: 16px;
  }
</style>
</head>
<body>

  <section class="label label--plain">
    <div class="label__header">
      <p class="alcohol">Deceiving% by vol.</p>
      <p class="vintage">2012</p>
      <p class="dedication">Foot Stomped and Bottled<br>for Nadia and Gus's</p>
      <p class="wine-type">Red Wine</p>
    </div>
    <div class="wordmark">
      <span class="wordmark__name">Fusaldi</span>
      <span class="wordmark__dot"></span>
    </div>
    <div class="label__footer">
      <p class="wedding-date">Wedding Day 9/28/13</p>
      <p class="volume">750 ml</p>
    </div>
  </section>

  <section class="label label--patterned">
    <div class="heart-pattern heart-pattern--left" role="img" aria-label="Repeating ivory and gold heart pattern border"></div>
    <div class="heart-pattern heart-pattern--right" role="img" aria-label="Repeating ivory and gold heart pattern border"></div>
    <div class="label__header">
      <p class="alcohol">Deceiving% by vol.</p>
      <p class="vintage">2012</p>
      <p class="dedication">Foot Stomped and Bottled<br>for Nadia and Gus's</p>
      <p class="wine-type">Red Wine</p>
    </div>
    <div class="wordmark">
      <span class="wordmark__name">Fusaldi</span>
      <span class="wordmark__dot"></span>
    </div>
    <div class="label__footer">
      <p class="wedding-date">Wedding Day 9/28/13</p>
      <p class="volume">750 ml</p>
    </div>
  </section>

</body>
</html>
```